Corvenne Jewelers Business Cards

A creative, cool edgy business card for our entire team that says we are a young, hip, luxury jewelry store specializing in diamonds and engagement rings but that we are also personal shoppers and trusted advisors. Our colors are Navy Blue & Platinum

I have included our past business card.

Font styles to use
Serif

Colors
0255a3

Requirements
Nice to have
• A card stock that you can write on with a pen

```html
<!DOCTYPE html>
<html lang="en">
<head>
<meta charset="utf-8">
<title>Corvenne Jewelers – Business Cards</title>
<link href="https://fonts.googleapis.com/css2?family=Cormorant+Garamond:wght@400;500&display=swap" rel="stylesheet">
<style>
  :root {
    --backdrop: #2b3263;
    --card-navy: #262c62;
    --platinum: #c9cad4;
    --platinum-soft: #a9abbd;
    --foil-light: rgba(214, 215, 222, 0.55);
    --foil-fade: rgba(214, 215, 222, 0);
  }
  * { margin: 0; padding: 0; box-sizing: border-box; }
  html, body {
    width: 1200px; height: 869px; overflow: hidden;
    background: var(--backdrop);
    font-family: "Cormorant Garamond", Georgia, serif;
  }
  .canvas { position: relative; width: 1200px; height: 869px; }
  .card {
    position: absolute; top: 208px;
    width: 296px; height: 518px;
    background: var(--card-navy);
    overflow: hidden;
  }
  .card--front { left: 266px; }
  .card--back { left: 639px; }

  .foil-decoration {
    position: absolute; left: 0; top: 0;
    width: 296px; height: 412px;
    background:
      radial-gradient(ellipse 62% 55% at 62% 52%, var(--foil-fade) 48%, var(--foil-light) 70%, var(--foil-fade) 88%);
  }

  .brand-name {
    position: absolute; left: 0; right: 0;
    text-align: center;
    font-variant: small-caps;
    font-weight: 500;
    color: var(--platinum);
    letter-spacing: 0.5px;
    white-space: nowrap;
  }
  .card--front .brand-name { top: 196px; font-size: 22px; }
  .card--back .brand-name { top: 462px; font-size: 27px; }

  .holder { position: absolute; left: 47px; top: 328px; }
  .holder__name {
    font-variant: small-caps; font-size: 22px; font-weight: 500;
    color: var(--platinum); letter-spacing: 0.4px; line-height: 1;
  }
  .holder__role { font-size: 16px; color: var(--platinum-soft); margin-top: 4px; }

  .contact-list { position: absolute; left: 47px; top: 397px; list-style: none; }
  .contact-list li {
    display: flex; align-items: center; gap: 6px;
    font-size: 13.5px; line-height: 17.5px; color: var(--platinum-soft);
    letter-spacing: 0.3px;
  }
  .contact-list svg { width: 10px; height: 10px; flex: none; }
  .contact-list svg * { fill: none; stroke: var(--platinum-soft); stroke-width: 1.1; }
</style>
</head>
<body>
<main class="canvas">
  <section class="card card--front">
    <p class="brand-name">Corvenne Jewelers</p>

    <div class="holder">
      <p class="holder__name">Julian Marlowe</p>
      <p class="holder__role">Director</p>
    </div>

    <ul class="contact-list">
      <li>
        <svg viewBox="0 0 10 10" aria-hidden="true"><path d="M2 1 L3.6 1 L4.2 3 L3.2 3.8 Q4.4 6 6.2 6.8 L7 5.8 L9 6.4 L9 8 Q5 9 2 5 Q1 3 2 1 Z"/></svg>
        555 218 4307
      </li>
      <li>
        <svg viewBox="0 0 10 10" aria-hidden="true"><rect x="2.5" y="0.6" width="5" height="8.8" rx="0.8"/><path d="M4.3 8 H5.7"/></svg>
        555 390 6614
      </li>
      <li>
        <svg viewBox="0 0 10 10" aria-hidden="true"><rect x="0.8" y="2.2" width="8.4" height="5.8"/><path d="M0.8 2.2 L5 5.6 L9.2 2.2"/></svg>
        jmarlowe@corvennejewelers.com
      </li>
      <li>
        <svg viewBox="0 0 10 10" aria-hidden="true"><circle cx="5" cy="5" r="4.2"/><ellipse cx="5" cy="5" rx="1.8" ry="4.2"/><path d="M0.8 5 H9.2"/></svg>
        www.corvennejewelers.com
      </li>
    </ul>
  </section>

  <section class="card card--back">
    <div class="foil-decoration" role="img" aria-label="Large platinum foil brand monogram decoration"></div>
    <p class="brand-name">Corvenne Jewelers</p>
  </section>
</main>
</body>
</html>
```